Business Card Design for company

We want new business cards. We'd like something different-- yet still highly professional. Our tagline is Providing leadership, delivering success. Stock photos are ok, as long as they are relevant and look upscale.

Target Market(s)

Architecture/Business Management Consulting/Engineering Consulting

Contact Information for Business Card

dark gray background with pops of blue might be good, but you tell me. You're the designers. Rounded corners might be nice, but again, you tell me.

Font styles to use
Serif
Sans Serif

Colors
3276b5
5c5c5c
9d9d9d
fbfbfb

Requirements
Nice to have
• Something different, but still very professional.

```html
<!DOCTYPE html>
<html lang="en">
<head>
<meta charset="utf-8">
<title>Norvane Consulting – Business Card</title>
<link rel="stylesheet" href="https://fonts.googleapis.com/css2?family=Work+Sans:wght@400;500;600&display=swap">
<style>
  :root {
    --brand-blue: #2b66a3;
    --brand-blue-deep: #1f4f7f;
    --ink: #4a4a4a;
    --ink-soft: #5c5c5c;
    --rule-light: #9d9d9d;
    --paper: #fbfbfb;
    --backdrop: #e6e8eb;
    --logo-light: #e9ecef;
  }
  * { box-sizing: border-box; margin: 0; padding: 0; }
  html, body { width: 1200px; height: 900px; overflow: hidden; }
  body {
    background: var(--backdrop);
    font-family: "Work Sans", Arial, sans-serif;
    display: flex;
    flex-direction: column;
    align-items: center;
    justify-content: center;
    gap: 40px;
  }
  .card {
    width: 700px;
    height: 400px;
    position: relative;
    box-shadow: 0 6px 20px rgba(0,0,0,.18);
  }

  /* Front */
  .card-front { background: var(--paper); }
  .wordmark {
    position: absolute;
    right: 60px;
    top: 120px;
    text-align: right;
    color: var(--brand-blue);
    font-weight: 600;
    text-transform: uppercase;
    letter-spacing: 3px;
    line-height: 1.05;
    font-size: 40px;
  }
  .wordmark .wordmark-sub { display: block; font-size: 22px; letter-spacing: 6px; }
  .details {
    position: absolute;
    left: 40px;
    bottom: 42px;
    display: flex;
    align-items: flex-end;
    gap: 22px;
  }
  .person { padding-bottom: 50px; }
  .person-name {
    color: var(--brand-blue);
    font-weight: 500;
    font-size: 17px;
    letter-spacing: 1.5px;
    text-transform: uppercase;
  }
  .person-title { color: var(--ink-soft); font-size: 13px; margin-top: 2px; }
  .divider { width: 1.5px; height: 80px; background: var(--brand-blue); }
  .contact-list { list-style: none; font-size: 13px; color: var(--ink); line-height: 1.7; }
  .contact-list li { display: flex; align-items: center; gap: 8px; }
  .contact-list svg { width: 10px; height: 10px; fill: var(--brand-blue); flex: none; }
  .contact-list .web-strong { color: var(--brand-blue); font-weight: 500; }
  .address { font-size: 13px; color: var(--ink); line-height: 1.5; font-style: normal; }

  /* Back */
  .card-back {
    background: linear-gradient(135deg, var(--brand-blue-deep), var(--brand-blue));
    display: flex;
    flex-direction: column;
    align-items: center;
    justify-content: center;
  }
  .wordmark-back {
    color: var(--logo-light);
    font-weight: 600;
    text-transform: uppercase;
    text-align: center;
    letter-spacing: 5px;
    font-size: 52px;
    line-height: 1.05;
  }
  .wordmark-back .wordmark-sub { display: block; font-size: 28px; letter-spacing: 9px; }
  .back-web {
    margin-top: 34px;
    display: flex;
    align-items: center;
    gap: 14px;
    color: var(--logo-light);
    font-size: 14px;
    letter-spacing: .5px;
  }
  .back-web .rule { width: 110px; height: 1px; background: rgba(233,236,239,.6); }
</style>
</head>
<body>

<section class="card card-front" aria-label="Card front">
  <div class="wordmark">Norvane<span class="wordmark-sub">Consulting</span></div>

  <div class="details">
    <div class="person">
      <p class="person-name">Daniel Hart</p>
      <p class="person-title">Director</p>
    </div>
    <span class="divider"></span>
    <ul class="contact-list">
      <li><svg viewBox="0 0 10 10" aria-hidden="true"><path d="M2 0.5l2 2-1 1.2c.6 1.3 1.6 2.3 2.8 2.8L7 5.5l2 2-1.2 1.8C4.5 9 1 5.5.7 2.2z"/></svg>(555) 014-2270</li>
      <li><svg viewBox="0 0 10 10" aria-hidden="true"><path d="M0 2h10v6H0zM1 3v.3l4 2.5 4-2.5V3L5 5.4z" fill-rule="evenodd"/></svg>hello@norvaneconsulting.com</li>
      <li><svg viewBox="0 0 10 10" aria-hidden="true"><circle cx="5" cy="5" r="4.5"/></svg>www.<span class="web-strong">norvaneconsulting</span>.com</li>
    </ul>
    <span class="divider"></span>
    <address class="address">48b Harlow Street,<br>Westbridge, 4021</address>
  </div>
</section>

<section class="card card-back" aria-label="Card back">
  <div class="wordmark-back">Norvane<span class="wordmark-sub">Consulting</span></div>
  <div class="back-web"><span class="rule"></span>www.norvaneconsulting.com<span class="rule"></span></div>
</section>

</body>
</html>
```